Name Card Design Project for a Japanese Restaurant

We need a name card design for our company. We run traditional japanese restaurant(Izakaya Concept) in singapore. We have 3 branches and one HQ. We would like to see designs that use the bright colour. Please visit
http://plaxtern.com/hanamori/ for our coming new website

Name Card 1:
Name: Tsuda Kenji
Position: Managing Director
Email Add: tsuda@hanamori.com.sg

Name Card 2: Name: Melissa Goh
Postion: Operation Manager
Email Add: melissa@hanamori.com.sg

Name Card 3:
Name: Vincent Goh
Position: Office Manager
Email Add: vincent@hanamori.com.sg

Name Card 4:
Name: Kimura Dai
Position: Executive Chef
Email Add: Leave it blank

Name Card 5:
Name: Satake Yumiko
Position: Executive Chef
Email Add: Leave it blank

Name Card 6:
Name: Leave it blank
Position: Leave it blank
Email Add: Leave it blank

Font Side:
Company Name: Hanamori Restaurant (Cedar Bend) Pte Ltd
Name:
Position:
Email Add:
Address: 37 Pellow Road #03-27 Singapore 084417
Tel: (65)64815732
Fax:(65) 64815718
Website: www.hanamori.com.sg

Back Side:
Kelvara Branch:
9 Teck Lorne Road #01-05B
Singapore 627315
(Starlanes)
Tel: 67359841

Marlow Crescent Branch:
14 Marlow Crescent #01-22/25
Singapore 057326
(Bukit Serai Exit C)
Tel:69217408

Rothmere Branch:
42 Keng Lim Road #01-09
(Fernhollow Court)
Singapore 318752
**New Outlet

Log in www.hanamori.com.sg for Bento Delivery Service
Updates

There is a typo mistake in the logo. Please use this to replace. Thanks 

      https://www.filequay.net/sh/4kdmwq82zr55plr/TQbnVeHrKc

Target Market(s)

working class people (weekdays) and family (weekends)

Industry/Entity Type

Restaurant

Requirements
Must have
• The name cards must use the logo we have attached

```html
<!DOCTYPE html>
<html lang="en">
<head>
<meta charset="utf-8">
<title>Hanamori Name Cards</title>
<link rel="stylesheet" href="https://fonts.googleapis.com/css2?family=Nunito+Sans:wght@400;700&display=swap">
<style>
  :root {
    --backdrop: #4b4b4b;
    --paper: #f7e8c9;
    --paper-deep: #efd9b0;
    --blossom: rgba(233, 168, 150, 0.45);
    --branch: rgba(190, 160, 130, 0.35);
    --ink: #1c1c1c;
    --accent: #d8261c;
  }
  * { box-sizing: border-box; margin: 0; padding: 0; }
  html, body { width: 900px; height: 1200px; overflow: hidden; }
  body {
    position: relative;
    background: var(--backdrop);
    font-family: "Nunito Sans", Verdana, sans-serif;
    color: var(--ink);
  }
  .icon-defs { position: absolute; width: 0; height: 0; }

  .card {
    position: absolute;
    width: 424px;
    height: 239px;
    background: linear-gradient(135deg, var(--paper) 0%, var(--paper-deep) 100%);
    overflow: hidden;
    box-shadow: 0 2px 6px rgba(0,0,0,0.35);
  }
  .col-left { left: 17px; }
  .col-right { left: 459px; }
  .row-1 { top: 138px; }
  .row-2 { top: 481px; }
  .row-3 { top: 824px; }

  .card-art {
    position: absolute;
    inset: 0;
    background:
      radial-gradient(ellipse 90px 70px at 395px 30px, var(--blossom), transparent 70%),
      radial-gradient(ellipse 120px 60px at 80px 8px, var(--blossom), transparent 70%),
      radial-gradient(ellipse 160px 110px at 300px 200px, var(--branch), transparent 70%);
  }

  .brand {
    position: absolute;
    left: 18px;
    top: 100px;
    width: 154px;
    text-align: center;
  }
  .brand-name {
    display: block;
    font-size: 27px;
    font-weight: 700;
    letter-spacing: 0.5px;
    line-height: 34px;
    color: var(--ink);
  }

  .details {
    position: absolute;
    left: 187px;
    top: 54px;
    font-size: 10.5px;
    line-height: 15.5px;
  }
  .person-name {
    font-size: 18px;
    font-weight: 400;
    letter-spacing: 0.4px;
    line-height: 22px;
  }
  .person-role { font-size: 10px; line-height: 14px; }
  .contact-line { display: flex; align-items: center; gap: 5px; }
  .company { margin-top: 17px; }
  .contact-line svg { width: 10px; height: 10px; flex: none; }
  .fax { margin-left: 6px; }
</style>
</head>
<body>
<svg class="icon-defs" aria-hidden="true">
  <defs>
    <symbol id="icon-mail" viewBox="0 0 10 10"><rect x="0.5" y="2" width="9" height="6.5" fill="#d8261c"/><path d="M0.5 2 L5 6 L9.5 2" fill="none" stroke="#f7e8c9" stroke-width="1"/></symbol>
    <symbol id="icon-phone" viewBox="0 0 10 10"><path d="M2 1 L4 1 L4.5 3.5 L3.3 4.3 Q4.5 6.5 6 7 L6.7 5.8 L9 6.3 L9 8.5 Q4 9.5 1.5 3 Z" fill="#d8261c"/></symbol>
    <symbol id="icon-fax" viewBox="0 0 10 10"><rect x="2.5" y="0.5" width="5" height="3" fill="#d8261c"/><rect x="0.5" y="4" width="9" height="5" fill="#d8261c"/><rect x="2.5" y="6" width="5" height="1" fill="#f7e8c9"/></symbol>
    <symbol id="icon-web" viewBox="0 0 10 10"><circle cx="5" cy="5" r="4.5" fill="#d8261c"/><path d="M0.5 5 H9.5 M5 0.5 Q2.5 5 5 9.5 M5 0.5 Q7.5 5 5 9.5" fill="none" stroke="#f7e8c9" stroke-width="0.7"/></symbol>
  </defs>
</svg>

<article class="card col-left row-1">
  <div class="card-art" role="img" aria-label="Faint cherry blossom branches on washi paper"></div>
  <div class="brand"><span class="brand-name">Hanamori</span></div>
  <div class="details">
    <p class="person-name">Tsuda Kenji</p>
    <p class="person-role">Managing Director</p>
    <p class="contact-line"><svg><use href="#icon-mail"/></svg>tsuda@hanamori.com.sg</p>
    <p class="company">Hanamori Restaurant (Cedar Bend) Pte Ltd</p>
    <p>37 Pellow Road #03-27 Singapore 084417</p>
    <p class="contact-line"><svg><use href="#icon-phone"/></svg>(65)64815732 <svg class="fax"><use href="#icon-fax"/></svg>(65) 64815718</p>
    <p class="contact-line"><svg><use href="#icon-web"/></svg>www.hanamori.com.sg</p>
  </div>
</article>

<article class="card col-right row-1">
  <div class="card-art" role="img" aria-label="Faint cherry blossom branches on washi paper"></div>
  <div class="brand"><span class="brand-name">Hanamori</span></div>
  <div class="details">
    <p class="person-name">Satake Yumiko</p>
    <p class="person-role">Executive Chef</p>
    <p class="contact-line"><svg><use href="#icon-mail"/></svg>blank@hanamori.com.sg</p>
    <p class="company">Hanamori Restaurant (Cedar Bend) Pte Ltd</p>
    <p>37 Pellow Road #03-27 Singapore 084417</p>
    <p class="contact-line"><svg><use href="#icon-phone"/></svg>(65)64815732 <svg class="fax"><use href="#icon-fax"/></svg>(65) 64815718</p>
    <p class="contact-line"><svg><use href="#icon-web"/></svg>www.hanamori.com.sg</p>
  </div>
</article>

<article class="card col-left row-2">
  <div class="card-art" role="img" aria-label="Faint cherry blossom branches on washi paper"></div>
  <div class="brand"><span class="brand-name">Hanamori</span></div>
  <div class="details">
    <p class="person-name">Vincent Goh</p>
    <p class="person-role">Office Manager</p>
    <p class="contact-line"><svg><use href="#icon-mail"/></svg>vincent@hanamori.com.sg</p>
    <p class="company">Hanamori Restaurant (Cedar Bend) Pte Ltd</p>
    <p>37 Pellow Road #03-27 Singapore 084417</p>
    <p class="contact-line"><svg><use href="#icon-phone"/></svg>(65)64815732 <svg class="fax"><use href="#icon-fax"/></svg>(65) 64815718</p>
    <p class="contact-line"><svg><use href="#icon-web"/></svg>www.hanamori.com.sg</p>
  </div>
</article>

<article class="card col-right row-2">
  <div class="card-art" role="img" aria-label="Faint cherry blossom branches on washi paper"></div>
  <div class="brand"><span class="brand-name">Hanamori</span></div>
  <div class="details">
    <p class="person-name">Kimura Dai</p>
    <p class="person-role">Executive Chef</p>
    <p class="contact-line"><svg><use href="#icon-mail"/></svg>blank@hanamori.com.sg</p>
    <p class="company">Hanamori Restaurant (Cedar Bend) Pte Ltd</p>
    <p>37 Pellow Road #03-27 Singapore 084417</p>
    <p class="contact-line"><svg><use href="#icon-phone"/></svg>(65)64815732 <svg class="fax"><use href="#icon-fax"/></svg>(65) 64815718</p>
    <p class="contact-line"><svg><use href="#icon-web"/></svg>www.hanamori.com.sg</p>
  </div>
</article>

<article class="card col-left row-3">
  <div class="card-art" role="img" aria-label="Faint cherry blossom branches on washi paper"></div>
  <div class="brand"><span class="brand-name">Hanamori</span></div>
  <div class="details">
    <p class="person-name">Melissa Goh</p>
    <p class="person-role">Operation Manager</p>
    <p class="contact-line"><svg><use href="#icon-mail"/></svg>melissa@hanamori.com.sg</p>
    <p class="company">Hanamori Restaurant (Cedar Bend) Pte Ltd</p>
    <p>37 Pellow Road #03-27 Singapore 084417</p>
    <p class="contact-line"><svg><use href="#icon-phone"/></svg>(65)64815732 <svg class="fax"><use href="#icon-fax"/></svg>(65) 64815718</p>
    <p class="contact-line"><svg><use href="#icon-web"/></svg>www.hanamori.com.sg</p>
  </div>
</article>

<article class="card col-right row-3">
  <div class="card-art" role="img" aria-label="Faint cherry blossom branches on washi paper"></div>
  <div class="brand"><span class="brand-name">Hanamori</span></div>
  <div class="details">
    <p class="person-name">Leave it blank</p>
    <p class="person-role">Leave it blank</p>
    <p class="contact-line"><svg><use href="#icon-mail"/></svg>blank@hanamori.com.sg</p>
    <p class="company">Hanamori Restaurant (Cedar Bend) Pte Ltd</p>
    <p>37 Pellow Road #03-27 Singapore 084417</p>
    <p class="contact-line"><svg><use href="#icon-phone"/></svg>(65)64815732 <svg class="fax"><use href="#icon-fax"/></svg>(65) 64815718</p>
    <p class="contact-line"><svg><use href="#icon-web"/></svg>www.hanamori.com.sg</p>
  </div>
</article>
</body>
</html>
```